OPRU Membership Certificate

We are launching an online membership for www.opru-members.example

When someone joins they will receive a membership certificate that outlines their name, membership number, membership status, date of membership

```html
<!DOCTYPE html>
<html lang="en">
<head>
<meta charset="utf-8">
<title>OPRU Membership Certificate</title>
<link rel="stylesheet" href="https://fonts.googleapis.com/css2?family=Cormorant+Garamond:wght@400&family=Montserrat:wght@500;600&family=Great+Vibes&display=swap">
<style>
  :root {
    --ink: #2a3550;
    --navy: #0b1838;
    --navy-deep: #06102a;
    --cream: #f6efc9;
    --paper: #ffffff;
    --gold-light: #f7e07a;
    --gold: #d9a520;
    --gold-dark: #9a5a0c;
    --white: #ffffff;
  }
  * { box-sizing: border-box; }
  html, body {
    margin: 0;
    padding: 0;
    width: 1200px;
    height: 872px;
    overflow: hidden;
    background: #ffffff;
  }
  .certificate {
    position: relative;
    width: 1200px;
    height: 872px;
    overflow: hidden;
    color: var(--ink);
    font-family: "Montserrat", Arial, sans-serif;
  }
  .certificate__backdrop {
    position: absolute;
    inset: 0;
  }
  .certificate__title {
    position: absolute;
    left: 88px;
    top: 92px;
    margin: 0;
    font-family: "Cormorant Garamond", Georgia, serif;
    font-weight: 400;
    font-size: 70px;
    line-height: 1;
    letter-spacing: 0.13em;
  }
  .certificate__subtitle {
    position: absolute;
    left: 92px;
    top: 174px;
    margin: 0;
    font-weight: 600;
    font-size: 30px;
    line-height: 1;
    letter-spacing: 0.06em;
  }
  .rule {
    position: absolute;
    height: 2px;
    background: var(--ink);
  }
  .rule--title { left: 96px; top: 227px; width: 405px; }
  .rule--name { left: 96px; top: 433px; width: 538px; }
  .rule--statement { left: 92px; top: 599px; width: 412px; }
  .certificate__lead {
    position: absolute;
    left: 98px;
    top: 276px;
    margin: 0;
    font-weight: 600;
    font-size: 25px;
    letter-spacing: 0.05em;
  }
  .certificate__name {
    position: absolute;
    left: 92px;
    top: 330px;
    margin: 0;
    font-family: "Great Vibes", cursive;
    font-weight: 400;
    font-size: 118px;
    line-height: 1;
  }
  .certificate__statement {
    position: absolute;
    left: 92px;
    top: 474px;
    margin: 0;
    font-weight: 500;
    font-size: 21px;
    line-height: 33px;
    letter-spacing: 0.07em;
  }
  .field {
    position: absolute;
    left: 92px;
    display: flex;
    align-items: flex-end;
    margin: 0;
    font-weight: 600;
    font-size: 18px;
    letter-spacing: 0.08em;
  }
  .field--number { top: 666px; }
  .field--status { top: 748px; left: 96px; }
  .field__blank {
    display: inline-block;
    width: 182px;
    height: 2px;
    margin-left: 8px;
    margin-bottom: 3px;
    background: var(--ink);
  }
  .field--number .field__blank { margin-left: 6px; }
  .field--status .field__blank { margin-left: 15px; }
  .signature {
    position: absolute;
    left: 808px;
    top: 745px;
    width: 238px;
    border-top: 2px solid var(--white);
    padding-top: 13px;
    text-align: center;
    color: var(--white);
    font-weight: 600;
    font-size: 19px;
    letter-spacing: 0.08em;
  }
  .seal__name {
    position: absolute;
    left: 883px;
    top: 156px;
    width: 200px;
    text-align: center;
    color: var(--white);
    font-weight: 600;
    font-size: 38px;
    line-height: 46px;
    letter-spacing: 0.08em;
  }
</style>
</head>
<body>
<main class="certificate">
  <svg class="certificate__backdrop" width="1200" height="872" viewBox="0 0 1200 872" aria-hidden="true">
    <defs>
      <linearGradient id="paperFade" x1="0" y1="0" x2="1" y2="0">
        <stop offset="0" stop-color="var(--paper)"/>
        <stop offset="1" stop-color="var(--cream)"/>
      </linearGradient>
      <linearGradient id="goldSweep" x1="0.55" y1="0" x2="0.75" y2="1">
        <stop offset="0" stop-color="var(--gold-light)"/>
        <stop offset="0.45" stop-color="var(--gold)"/>
        <stop offset="1" stop-color="var(--gold-dark)"/>
      </linearGradient>
      <linearGradient id="ribbonGold" x1="0" y1="0" x2="1" y2="0">
        <stop offset="0" stop-color="#e9c451"/>
        <stop offset="0.5" stop-color="#f6dd74"/>
        <stop offset="1" stop-color="#c8931f"/>
      </linearGradient>
      <linearGradient id="ringGold" x1="0" y1="0" x2="1" y2="1">
        <stop offset="0" stop-color="#f6dc72"/>
        <stop offset="0.5" stop-color="#c98f22"/>
        <stop offset="1" stop-color="#f2d46a"/>
      </linearGradient>
      <linearGradient id="navyShade" x1="0" y1="0" x2="1" y2="1">
        <stop offset="0" stop-color="var(--navy)"/>
        <stop offset="1" stop-color="var(--navy-deep)"/>
      </linearGradient>
    </defs>

    <rect class="gold-field" width="1200" height="872" fill="url(#goldSweep)"/>
    <path class="paper-arc" d="M0,0 H647 C775,120 830,300 812,470 C798,640 720,790 630,872 H0 Z" fill="url(#paperFade)"/>
    <path class="navy-field" d="M1047,0 H1200 V872 H630 C860,700 1010,460 1047,0 Z" fill="url(#navyShade)"/>

    <rect class="inner-frame" x="40" y="36" width="1116" height="796" fill="none" stroke="var(--white)" stroke-width="2"/>

    <path class="ribbon" d="M921,0 H1047 V375 L983,325 L921,375 Z" fill="url(#ribbonGold)"/>
    <circle class="seal__ring" cx="983" cy="179" r="119" fill="url(#ringGold)"/>
    <circle class="seal__inner-ring" cx="983" cy="179" r="101" fill="#f3d463"/>
    <circle class="seal__core" cx="983" cy="179" r="90" fill="var(--navy)"/>
  </svg>

  <div class="seal__name">OPRU</div>

  <h1 class="certificate__title">CERTIFICATE</h1>
  <p class="certificate__subtitle">OF MEMBERSHIP</p>
  <div class="rule rule--title"></div>

  <p class="certificate__lead">This Certifies that</p>
  <p class="certificate__name">Name Surname</p>
  <div class="rule rule--name"></div>

  <p class="certificate__statement">
    has been duly admitted as a member of<br>
    ONLINE PROFESSIONAL RECOGNITION UNION<br>
    this day of [Date Day/Month/Year].
  </p>
  <div class="rule rule--statement"></div>

  <p class="field field--number">MEMBERSHIP NUMBER:<span class="field__blank"></span></p>
  <p class="field field--status">MEMBERSHIP STATUS:<span class="field__blank"></span></p>

  <div class="signature">SIGNATURE</div>
</main>
</body>
</html>
```